Poster Design

Hello,

My name is Rowan Pickett and I run a vidora channel called 'CrumbleDiary'. I want a poster made for those who watch my video to purchase and put on their wall at home. The poster will be all text and as you can see, I've attached a few examples of posters which I would like it to be similar to. I use a lot of the colour #ab6f7f so it would be good to incorporate this in somewhere (maybe the background colour).
I would like the poster to say:
"Do More Of What Makes YOU Happy"
I need this poster to be for sale ready for christmas, so Im going to need the designs created as soon as possible. Im sorry for the rush.
Have fun with it and feel free to upload multiple versions of a design as well as a few designs if you like.
I look forward to seeing what you come up with.
Rowan
(Of course I will need to own all rights once the payment has been made)

```html
<!DOCTYPE html>
<html lang="en">
<head>
<meta charset="utf-8">
<title>Do More Of What Makes You Happy — Poster</title>
<link rel="stylesheet" href="https://fonts.googleapis.com/css2?family=Anton&family=Courier+Prime&family=Alfa+Slab+One&family=Comfortaa:wght@500&family=Caveat+Brush&display=swap">
<style>
  :root {
    --brand-mauve: #ab6f7f;
    --rose-glow: rgba(226, 160, 186, 0.75);
    --rose-soft: rgba(214, 140, 172, 0.6);
    --rose-deep: #b24a7c;
    --ink-white: #ffffff;
    --stitch-fill: #ebe0e5;
    --ornament-glow: rgba(255, 255, 255, 0.28);
    --shadow: rgba(90, 30, 55, 0.4);
  }
  html, body {
    margin: 0;
    padding: 0;
    overflow: hidden;
  }
  .poster {
    position: relative;
    width: 848px;
    height: 1200px;
    overflow: hidden;
    background:
      radial-gradient(ellipse 480px 420px at 25% 22%, var(--rose-glow), transparent 72%),
      radial-gradient(ellipse 460px 380px at 72% 55%, var(--rose-soft), transparent 72%),
      radial-gradient(ellipse 420px 360px at 30% 85%, var(--rose-soft), transparent 72%),
      radial-gradient(ellipse 480px 380px at 100% 100%, var(--rose-deep), transparent 70%),
      var(--brand-mauve);
  }
  .line {
    position: absolute;
    left: 0;
    width: 100%;
    margin: 0;
    text-align: center;
    color: var(--ink-white);
    line-height: 1;
    white-space: nowrap;
  }
  .line--do-more {
    top: 118px;
    font-family: "Anton", "Impact", sans-serif;
    font-size: 136px;
    letter-spacing: 1px;
    text-shadow: 2px 3px 4px var(--shadow);
  }
  .line--of-what {
    top: 284px;
    font-family: "Courier Prime", "Courier New", monospace;
    font-size: 104px;
    letter-spacing: 2px;
    color: transparent;
    -webkit-text-stroke: 2.5px var(--ink-white);
    text-shadow: 1px 2px 3px var(--shadow);
  }
  .line--makes {
    top: 400px;
    font-family: "Alfa Slab One", "Rockwell", serif;
    font-size: 122px;
    color: var(--stitch-fill);
    -webkit-text-stroke: 2px var(--ink-white);
    text-shadow: 2px 3px 4px var(--shadow);
  }
  .you-row {
    position: absolute;
    left: 0;
    top: 570px;
    width: 848px;
    height: 160px;
  }
  .you-row__ornaments {
    position: absolute;
    inset: 0;
    background:
      radial-gradient(circle 80px at 271px 80px, var(--ornament-glow), transparent 100%),
      radial-gradient(circle 80px at 424px 80px, var(--ornament-glow), transparent 100%),
      radial-gradient(circle 80px at 594px 80px, var(--ornament-glow), transparent 100%);
  }
  .you-row__letter {
    position: absolute;
    top: 22px;
    width: 100px;
    margin-left: -50px;
    text-align: center;
    font-family: "Comfortaa", sans-serif;
    font-weight: 500;
    font-size: 84px;
    line-height: 1;
    color: var(--ink-white);
    text-shadow: 1px 2px 3px var(--shadow);
  }
  .you-row__letter--y { left: 271px; }
  .you-row__letter--o { left: 424px; }
  .you-row__letter--u { left: 594px; }
  .line--happy {
    top: 768px;
    font-family: "Caveat Brush", cursive;
    font-size: 290px;
    letter-spacing: 12px;
    text-shadow: 2px 3px 4px var(--shadow);
  }
</style>
</head>
<body>
  <main class="poster">
    <h1 class="line line--do-more">DO MORE</h1>
    <p class="line line--of-what">OF WHAT</p>
    <p class="line line--makes">MAKES</p>

    <div class="you-row">
      <div class="you-row__ornaments" role="img" aria-label="Dotted circle ornaments framing each letter of the word you"></div>
      <span class="you-row__letter you-row__letter--y">y</span>
      <span class="you-row__letter you-row__letter--o">o</span>
      <span class="you-row__letter you-row__letter--u">u</span>
    </div>

    <p class="line line--happy">Happy</p>
  </main>
</body>
</html>
```